Renewable energy company needs modern memorable marketing brochure

We have an 8 page marketing brochure which was created in house. This needs to be revamped and modernised to stand out from our competitors in Australia, Chile and the UK. The brochure should depict us as a professional and dynamic company and instil confidence in prospective clients that we do a professional job. Once the design is finalised we will need a country specific document in the correct language i.e. Spanish for Chile. We are happy to pay for these iterations. We have a company logo which we would like incorporated into the brochure and the colours from the logo utilised where appropriate in the overall design. I have uploaded our existing brochure for an example of the content that the brochure needs to have and can upload the images separately if they are needed. Images in the brochure need to be copyright free and we have lots of photos in-house. I have added all the images from the last brochure and also the text in Indesign so it can be copied easily if needed.

Target Market(s)

landowners and companies

Industry/Entity Type

It Company

Requirements
Must have
• A clean modern look with some colours taken from the logo colour. Be easy to print in various countries.

```html
<!DOCTYPE html>
<html lang="en">
<head>
<meta charset="utf-8">
<title>Infinite Energy – Radiant Fields Brochure Cover</title>
<link href="https://fonts.googleapis.com/css2?family=Lato:wght@400;700&display=swap" rel="stylesheet">
<style>
  :root {
    --backdrop: #ecebe7;
    --paper: #ffffff;
    --footer-grey: #f1f2f2;
    --teal: #2b9c88;
    --teal-light: #38a897;
    --navy: #17263a;
    --ink-grey: #55606b;
    --sky-top: #3e78b8;
    --sky-mid: #9fb8cf;
    --horizon: #e7b49a;
    --panel-dark: #1c2c58;
    --panel-light: #5b76a8;
  }
  html, body {
    margin: 0;
    padding: 0;
    width: 1200px;
    height: 803px;
    overflow: hidden;
    background: var(--backdrop);
    font-family: "Lato", Arial, sans-serif;
  }
  .brochure-cover {
    position: absolute;
    left: 338px;
    top: 31px;
    width: 524px;
    height: 741px;
    background: var(--paper);
    box-shadow: 0 4px 18px rgba(0,0,0,0.18);
    overflow: hidden;
  }
  .cover-shapes {
    position: absolute;
    inset: 0;
    width: 524px;
    height: 741px;
  }
  .cover-title {
    position: absolute;
    left: 52px;
    top: 438px;
    margin: 0;
    color: var(--paper);
    font-weight: 700;
    font-size: 38px;
    letter-spacing: 0.5px;
    text-transform: uppercase;
  }
  .cover-subtitle {
    position: absolute;
    left: 54px;
    top: 492px;
    margin: 0;
    width: 320px;
    color: var(--navy);
    font-weight: 700;
    font-size: 16px;
    line-height: 1.3;
    text-transform: uppercase;
  }
  .brand {
    position: absolute;
    left: 30px;
    bottom: 28px;
    display: flex;
    align-items: center;
    gap: 10px;
  }
  .brand-dot {
    width: 38px;
    height: 38px;
    border-radius: 50%;
    background: var(--teal);
  }
  .brand-name {
    color: var(--navy);
    font-size: 15px;
    font-weight: 400;
    line-height: 1.05;
    text-transform: uppercase;
    letter-spacing: 0.5px;
  }
  .web-address {
    position: absolute;
    right: 28px;
    bottom: 88px;
    color: var(--ink-grey);
    font-size: 11px;
  }
</style>
</head>
<body>
  <main class="brochure-cover">
    <svg class="cover-shapes" viewBox="0 0 524 741" aria-hidden="false">
      <defs>
        <linearGradient id="photoTone" x1="0" y1="0" x2="0" y2="1">
          <stop offset="0" stop-color="var(--sky-top)"/>
          <stop offset="0.22" stop-color="var(--sky-mid)"/>
          <stop offset="0.34" stop-color="var(--horizon)"/>
          <stop offset="0.40" stop-color="var(--panel-light)"/>
          <stop offset="1" stop-color="var(--panel-dark)"/>
        </linearGradient>
        <linearGradient id="tealBand" x1="0" y1="0" x2="1" y2="0">
          <stop offset="0" stop-color="var(--teal)"/>
          <stop offset="1" stop-color="var(--teal-light)"/>
        </linearGradient>
      </defs>
      <path class="cover-photo" role="img" aria-label="Photograph of a large field of solar panels stretching to the horizon under a dusk sky"
            d="M0 0 H524 V362 L0 398 Z" fill="url(#photoTone)"/>
      <path class="teal-band" d="M0 408 L524 372 V612 L0 652 Z" fill="url(#tealBand)"/>
      <path class="footer-strip" d="M0 652 L524 612 V741 H0 Z" fill="var(--footer-grey)"/>
    </svg>

    <h1 class="cover-title">Infinite Energy</h1>
    <p class="cover-subtitle">Use your land to harvest energy from the sun</p>

    <div class="web-address">www.radiantfields.com.au</div>

    <div class="brand">
      <div class="brand-dot"></div>
      <div class="brand-name">Radiant<br>Fields</div>
    </div>
  </main>
</body>
</html>
```